Business Card For Kelmora Financial Consulting

Hi, I would like a business card designed. Bold, modern.
Please use the same design as the logo. I have also attached the website design to see the overall theme.
Wordmark Font
Color: Hex: #01AEF7

```html
<!DOCTYPE html>
<html lang="en">
<head>
<meta charset="utf-8">
<title>Kelmora Consulting – Business Card</title>
<link rel="stylesheet" href="https://fonts.googleapis.com/css2?family=Barlow+Condensed:wght@700&family=Montserrat:wght@600&family=Questrial&display=swap">
<style>
  :root {
    --paper: #ffffff;
    --brand-blue: #0098d7;
    --band-blue: #2ea6e0;
    --ink-dark: #19222b;
    --text-light: #f3f3f3;
    --icon-dark: #1a222b;
  }
  * { margin: 0; padding: 0; box-sizing: border-box; }
  html, body {
    width: 1200px; height: 1200px; overflow: hidden;
    background: var(--paper);
  }
  .sheet { position: relative; width: 1200px; height: 1200px; }
  .card {
    position: absolute; left: 144px;
    width: 920px; height: 525px;
    background: var(--brand-blue);
    overflow: hidden;
    box-shadow: 0 4px 18px rgba(0,0,0,0.12);
  }
  .card--front { top: 55px; }
  .card--back { top: 634px; }
  .card__shapes { position: absolute; inset: 0; width: 920px; height: 525px; }

  .brandmark {
    position: absolute; left: 86px; top: 371px;
    display: flex; align-items: flex-start; gap: 9px;
  }
  .brandmark__square {
    width: 41px; height: 41px; margin-top: 3px;
    border: 3px solid var(--brand-blue);
  }
  .brandmark__name {
    font-family: "Montserrat", sans-serif; font-weight: 600;
    color: var(--text-light); line-height: 1;
  }
  .brandmark__word { display: block; font-size: 34px; letter-spacing: 1px; }
  .brandmark__tag { display: block; font-size: 9px; letter-spacing: 11.6px; margin-top: 5px; }

  .title {
    position: absolute; left: 472px; top: 38px;
    color: var(--text-light);
  }
  .title__name {
    font-family: "Barlow Condensed", sans-serif; font-weight: 700;
    font-size: 52px; letter-spacing: 1px; line-height: 1;
  }
  .title__sub {
    display: flex; align-items: center; gap: 16px; margin-top: 6px;
    font-family: "Questrial", sans-serif; font-size: 21px; letter-spacing: 2px;
  }
  .title__rule { width: 166px; height: 1px; background: var(--text-light); }

  .contact {
    position: absolute; left: 488px; top: 181px;
    list-style: none;
    font-family: "Questrial", sans-serif; color: var(--text-light);
    font-weight: 700;
  }
  .contact__item { display: flex; align-items: center; gap: 16px; }
  .contact__icon { width: 22px; height: 22px; flex: none; fill: var(--icon-dark); }
  .contact__text { letter-spacing: 2px; line-height: 1.2; }
  .contact__item--address .contact__text span { display: block; }
  .contact__item--address .contact__line1 { font-size: 19px; }
  .contact__item--address .contact__line2 { font-size: 23px; }
  .contact__item--phone { margin-top: 10px; font-size: 24px; }
  .contact__item--email { margin-top: 12px; font-size: 24px; letter-spacing: 1px; }

  .social {
    position: absolute; left: 751px; top: 458px;
    display: flex; gap: 8px; list-style: none;
  }
  .social__dot {
    width: 26px; height: 26px; border-radius: 50%;
    background: #3b4147;
  }
</style>
</head>
<body>
<main class="sheet">

  <section class="card card--front" aria-label="Business card front">
    <svg class="card__shapes" viewBox="0 0 1472 840" preserveAspectRatio="none" aria-hidden="true">
      <polygon fill="var(--band-blue)" points="0,145 318,320 537,442 1255,840 0,840"/>
      <polygon fill="var(--ink-dark)" points="0,200 270,345 318,320 537,437 537,497 1157,840 0,840"/>
    </svg>

    <div class="brandmark">
      <div class="brandmark__square"></div>
      <p class="brandmark__name">
        <span class="brandmark__word">KELMORA</span>
        <span class="brandmark__tag">CONSULTING</span>
      </p>
    </div>

    <header class="title">
      <h1 class="title__name">KELMORA</h1>
      <p class="title__sub">CONSULTING <span class="title__rule"></span></p>
    </header>

    <ul class="contact">
      <li class="contact__item contact__item--address">
        <svg class="contact__icon" viewBox="0 0 24 24" aria-hidden="true"><path d="M12 1a8 8 0 0 0-8 8c0 6 8 14 8 14s8-8 8-14a8 8 0 0 0-8-8zm0 11a3 3 0 1 1 0-6 3 3 0 0 1 0 6z"/></svg>
        <p class="contact__text"><span class="contact__line1">123 Lorem Ipsum Dolor</span><span class="contact__line2">Type Address here</span></p>
      </li>
      <li class="contact__item contact__item--phone">
        <svg class="contact__icon" viewBox="0 0 24 24" aria-hidden="true"><path d="M6.6 10.8a15.1 15.1 0 0 0 6.6 6.6l2.2-2.2a1 1 0 0 1 1-.25 11.4 11.4 0 0 0 3.6.57 1 1 0 0 1 1 1V20a1 1 0 0 1-1 1A17 17 0 0 1 3 4a1 1 0 0 1 1-1h3.5a1 1 0 0 1 1 1c0 1.25.2 2.45.57 3.57a1 1 0 0 1-.25 1z"/></svg>
        <p class="contact__text">+1 888 555 0142</p>
      </li>
      <li class="contact__item contact__item--email">
        <svg class="contact__icon" viewBox="0 0 24 24" aria-hidden="true"><path d="M2 5h20v15H2zm2.5 2.5V18h2.5v-7l5 4.5 5-4.5v7h2.5V7.5h-1.5L12 13 5.5 7.5z"/></svg>
        <p class="contact__text">kelmoracon@mail.com</p>
      </li>
    </ul>

    <ul class="social" aria-label="Social profiles">
      <li class="social__dot"></li>
      <li class="social__dot"></li>
      <li class="social__dot"></li>
      <li class="social__dot"></li>
    </ul>
  </section>

  <section class="card card--back" aria-label="Business card back">
    <svg class="card__shapes" viewBox="0 0 1472 840" preserveAspectRatio="none" aria-hidden="true">
      <polygon fill="var(--band-blue)" points="0,145 318,320 537,442 1255,840 0,840"/>
      <polygon fill="var(--ink-dark)" points="0,200 270,345 318,320 537,437 537,497 1157,840 0,840"/>
    </svg>

    <div class="brandmark">
      <div class="brandmark__square"></div>
      <p class="brandmark__name">
        <span class="brandmark__word">KELMORA</span>
        <span class="brandmark__tag">CONSULTING</span>
      </p>
    </div>
  </section>

</main>
</body>
</html>
```